Tarnwick Tax Advisers Business Card

We are seeking a clean, professional, and modern double sided business card design for Tarnwick Tax Advisers, a tax, accounting, and advisory firm serving business owners, professionals, and investors.
The design should convey credibility, precision, trust, and sophistication appropriate for a CPA level tax advisory firm. Avoid playful, trendy, or overly decorative styles. The look should be sharp, balanced, and timeless.
Our official company logo has been uploaded, which must be incorporated appropriately and consistently with the brand. Designers should not modify, distort, or recreate the logo.
Card format
Standard US business card size (3.5 x 2 inches)
Double sided
Design direction
Professional and modern
Minimalist and uncluttered
Strong typography and clean spacing
Subtle visual interest is welcome, but simplicity is preferred
High contrast and readability are critical
Front side
Primary focus on the Tarnwick Tax Advisers logo
The firm name should be clearly legible and visually prominent
Background may be white or dark, depending on what best complements the logo
Back side
Contact information layout, such as
Name: Martin G. Pellow, MSA, CFP®, AIF®, EA
Title: Managing Director, Tax
Email: mpellow@mytarnwickfirm.net
Website: https://www.tarnwickfirm-example.tax/
Mobile: (480) 555-0132
Direct: (817) 555-0187
Main: (817) 555-0149
Address: 3807 Fenwick Rd., Suite 118, Grapevine, TX 76099
Icons may be used sparingly if they enhance clarity
The layout should feel organized and structured
Color and style
Use colors that complement the uploaded logo
Neutral, professional tones preferred
Avoid loud or saturated colors
The design should print well on standard cardstock
Print considerations
Design should be print‑ready
No edge to edge elements that risk being cut off
Proper margins and bleed awareness
Overall, the goal is a polished, high end business card that reflects trust, expertise, and professionalism consistent with a firm providing tax strategy, compliance, and advisory services.

```html
<!DOCTYPE html>
<html lang="en">
<head>
<meta charset="utf-8">
<title>Tarnwick Tax Advisers – Business Card</title>
<link rel="stylesheet" href="https://fonts.googleapis.com/css2?family=Montserrat:wght@600&family=Roboto:wght@400;500;700&display=swap">
<style>
  :root {
    --navy: #22265a;
    --white: #ffffff;
    --paper: #fdfdfd;
    --backdrop: #e3e5e7;
    --accent: #e0784a;
    --muted: #b7bad6;
    --rule: rgba(255, 255, 255, 0.28);
  }
  * { margin: 0; padding: 0; box-sizing: border-box; }
  html, body {
    width: 1200px; height: 1200px; overflow: hidden;
    background: var(--backdrop);
    font-family: "Roboto", Arial, sans-serif;
  }
  .canvas { position: relative; width: 1200px; height: 1200px; }
  .card {
    position: absolute; left: 191px; width: 817px; height: 473px; overflow: hidden;
  }
  .card--front { top: 96px; background: var(--paper); }
  .card--back { top: 630px; background: var(--navy); color: var(--white); }

  .brand {
    position: absolute; display: flex; align-items: center;
    font-family: "Montserrat", Arial, sans-serif; font-weight: 600;
    white-space: nowrap;
  }
  .brand__dot { border-radius: 50%; flex: none; }
  .card--front .brand {
    left: 129px; width: 559px; top: 150px; height: 80px;
    justify-content: center; gap: 18px; color: var(--navy); font-size: 44px;
  }
  .card--front .brand__dot { width: 30px; height: 30px; background: var(--navy); }
  .front__rule {
    position: absolute; left: 129px; width: 559px; top: 360px;
    height: 2px; background: var(--navy);
  }

  .card--back .brand {
    left: 48px; top: 60px; gap: 10px; color: var(--white); font-size: 22px;
  }
  .card--back .brand__dot { width: 16px; height: 16px; background: var(--white); }

  .contact { position: absolute; left: 419px; top: 0; width: 360px; }
  .contact__name {
    position: absolute; top: 66px; white-space: nowrap;
    font-weight: 700; font-size: 25px;
  }
  .contact__creds { font-weight: 500; font-size: 16px; }
  .contact__creds sup { font-size: 9px; }
  .contact__title {
    position: absolute; top: 103px; font-size: 21px; color: var(--muted);
  }
  .row {
    position: absolute; left: 0; display: flex; align-items: center;
    gap: 19px; font-size: 21.5px; line-height: 1; white-space: nowrap;
  }
  .row--small { font-size: 18px; }
  .row svg { width: 21px; height: 21px; flex: none; }
  .row--address { align-items: flex-start; line-height: 29px; font-size: 21px; }
  .row--address svg { margin-top: 4px; }
  .divider {
    position: absolute; left: 0; width: 351px; height: 1.5px; background: var(--rule);
  }
</style>
</head>
<body>
<main class="canvas">
  <section class="card card--front" aria-label="Card front">
    <div class="brand"><span class="brand__dot"></span>Tarnwick Tax Advisers</div>
    <div class="front__rule"></div>
  </section>

  <section class="card card--back" aria-label="Card back">
    <div class="brand"><span class="brand__dot"></span>Tarnwick Tax Advisers</div>

    <div class="contact">
      <p class="contact__name">Martin G. Pellow, <span class="contact__creds">MSA, CFP<sup>®</sup>, AIF<sup>®</sup>, EA</span></p>
      <p class="contact__title">Managing Director, Tax</p>

      <p class="row" style="top:162px">
        <svg viewBox="0 0 24 24" fill="none" stroke="var(--accent)" stroke-width="1.5"><rect x="6.5" y="2" width="11" height="20" rx="2"/><line x1="11" y1="18.5" x2="13" y2="18.5"/></svg>
        Mobile: (480) 555-0132
      </p>
      <p class="row" style="top:193px">
        <svg viewBox="0 0 24 24" fill="none" stroke="var(--accent)" stroke-width="1.5" stroke-linejoin="round"><path d="M5 3h4l2 5-2.5 1.5a11 11 0 0 0 6 6L16 13l5 2v4a2 2 0 0 1-2 2A17 17 0 0 1 3 5a2 2 0 0 1 2-2z"/></svg>
        Direct: (817) 555-0187
      </p>
      <p class="row" style="top:224px">
        <svg viewBox="0 0 24 24" fill="none" stroke="var(--accent)" stroke-width="1.5" stroke-linejoin="round"><path d="M5 3h4l2 5-2.5 1.5a11 11 0 0 0 6 6L16 13l5 2v4a2 2 0 0 1-2 2A17 17 0 0 1 3 5a2 2 0 0 1 2-2z"/></svg>
        Main: (817) 555-0149
      </p>

      <div class="divider" style="top:266px"></div>

      <p class="row row--small" style="top:286px">
        <svg viewBox="0 0 24 24" fill="none" stroke="var(--accent)" stroke-width="1.5" stroke-linejoin="round"><rect x="2.5" y="5" width="19" height="14" rx="1"/><path d="M3 6l9 7 9-7"/></svg>
        mpellow@mytarnwickfirm.net
      </p>
      <p class="row row--small" style="top:317px">
        <svg viewBox="0 0 24 24" fill="none" stroke="var(--accent)" stroke-width="1.5"><circle cx="12" cy="12" r="9.5"/><ellipse cx="12" cy="12" rx="4" ry="9.5"/><line x1="2.5" y1="12" x2="21.5" y2="12"/><path d="M4 7h16M4 17h16"/></svg>
        https://www.tarnwickfirm-example.tax/
      </p>

      <div class="divider" style="top:357px"></div>

      <p class="row row--address" style="top:372px">
        <svg viewBox="0 0 24 24" fill="none" stroke="var(--accent)" stroke-width="1.5" stroke-linejoin="round"><path d="M12 22s7-7.2 7-12.5A7 7 0 0 0 5 9.5C5 14.8 12 22 12 22z"/><circle cx="12" cy="9.5" r="2.6"/></svg>
        <span>3807 Fenwick Rd., Suite 118<br>Grapevine, TX 76099</span>
      </p>
    </div>
  </section>
</main>
</body>
</html>
```